UVANTA Virtualizing the computer, making it live in the cloud

We plan to visualize the computer, essentially making all your computing, storage, security, processing, etc done in the cloud. We feel this will revolutionize the entire computer industry.
We have a logo design which has been included here. We want this sharp, progressive and also frameworked in a way that we can sell our monthly service as well as computers online through this site.

Target Market(s)

Laptop users, Millennials, college educated people.

Industry/Entity Type

Computer

Number of Pages Required

5+ page

Font styles to use
Serif
Sans Serif

Colors

Designer to choose colors to be used in the design.

Requirements
Must have
• eCommerce capable. Frameworked for people to enroll in our program and pay for the service online. Would prefer to allow people from multiple countries to enroll and use our service

```html
<!DOCTYPE html>
<html lang="en">
<head>
<meta charset="utf-8">
<title>UVANTA — Virtualizing the Computer</title>
<link href="https://fonts.googleapis.com/css2?family=Montserrat:wght@400;500;600;700;800&family=Open+Sans:wght@400;600;700&family=Fira+Sans:ital,wght@1,600;1,700&display=swap" rel="stylesheet">
<style>
:root{
  --gold:#e0bd00;
  --gold-deep:#c9a800;
  --black:#0b0b0b;
  --ink:#1c1c1c;
  --grey-bg:#efefef;
  --card-grey:#ececec;
  --line:#d2d2d2;
  --white:#ffffff;
  --muted:#9a9a9a;
  --green:#7cb518;
}
*{margin:0;padding:0;box-sizing:border-box}
html,body{width:1200px;height:3109px;overflow:hidden}
body{position:relative;background:var(--white);font-family:"Open Sans",Arial,sans-serif;color:var(--ink)}
.abs{position:absolute}
.heading{font-family:"Montserrat",Arial,sans-serif}

/* header */
.site-header{position:absolute;left:0;top:0;width:1200px;height:124px;background:rgba(0,0,0,.92);border-bottom:2px solid var(--gold);z-index:5}
.contact-tab{position:absolute;left:642px;top:0;width:518px;height:42px;background:var(--gold);clip-path:polygon(0 0,100% 0,100% 100%,24px 100%);display:flex;align-items:center;padding-left:62px;gap:54px;font:600 13px "Open Sans",sans-serif;color:var(--black)}
.contact-tab span{display:flex;align-items:center;gap:10px}
.tab-icon{width:20px;height:20px;border:2px solid var(--black);border-radius:50%;display:inline-flex;align-items:center;justify-content:center}
.tab-social{display:flex;gap:4px}
.tab-social i{width:17px;height:17px;border:2px solid var(--black);border-radius:50%;display:block}
.brand{position:absolute;display:flex;align-items:center;gap:10px;font-family:"Montserrat",sans-serif;font-weight:700;color:var(--white);letter-spacing:1px}
.brand .dot{border-radius:50%;background:var(--gold);flex:none}
.site-header .brand{left:68px;top:66px;font-size:34px}
.site-header .brand .dot{width:18px;height:18px}
.main-nav{position:absolute;left:586px;top:84px;display:flex;gap:0;font:600 12px "Montserrat",sans-serif;color:var(--white)}
.main-nav a{color:inherit;text-decoration:none;position:absolute;white-space:nowrap}
.main-nav a.active{color:var(--gold)}
.demo-btn{position:absolute;left:1011px;top:72px;width:141px;height:36px;background:var(--gold);border-radius:3px;font:600 13px "Open Sans",sans-serif;color:var(--black);display:flex;align-items:center;justify-content:center}

/* hero */
.hero{position:absolute;left:0;top:0;width:1200px;height:660px}
.hero-photo{position:absolute;inset:0;background:radial-gradient(ellipse 420px 300px at 560px 330px,#5a7fb0 0%,#28426c 40%,#0f1e36 75%,#0a1220 100%)}
.hero-title{position:absolute;left:0;top:368px;width:1200px;text-align:center;font:700 35px "Montserrat",sans-serif;color:var(--gold);letter-spacing:.3px;text-shadow:0 2px 6px rgba(0,0,0,.5)}
.hero-cta{position:absolute;left:489px;top:431px;width:222px;height:48px;border:2px solid var(--gold);background:rgba(0,0,0,.45);font:700 19px "Montserrat",sans-serif;color:var(--gold);display:flex;align-items:center;justify-content:center;letter-spacing:.5px}

/* feature band */
.feature-band{position:absolute;left:0;top:660px;width:1200px;height:175px;background:linear-gradient(#2a2622,#151311)}
.band-title{position:absolute;left:68px;top:705px;font:700 42px "Montserrat",sans-serif;color:var(--gold);line-height:1}
.band-sub{position:absolute;left:68px;top:759px;font:700 22px "Montserrat",sans-serif;color:var(--white)}
.band-sub b{color:var(--gold)}
.feature{position:absolute;top:690px;width:120px;text-align:center}
.feature .ring{width:80px;height:80px;margin:0 auto;border:4px solid var(--gold);border-radius:50%;display:flex;align-items:center;justify-content:center;background:#111}
.feature .label{margin-top:12px;font:600 12px "Montserrat",sans-serif;color:var(--white)}

/* section headings */
.sec-title{position:absolute;left:0;width:1200px;display:flex;align-items:center;justify-content:center;gap:16px;font:700 23px "Montserrat",sans-serif}
.sec-title .rule{width:110px;height:1px;background:var(--line)}
.sec-title .mark{width:30px;height:30px;border:4px solid var(--gold);border-radius:50%}

/* about */
.about-text{position:absolute;left:97px;top:972px;width:1006px;text-align:center;font-size:13.3px;line-height:21.5px;color:#333}
.learn-btn{position:absolute;left:505px;top:1094px;width:191px;height:42px;background:var(--ink);border-radius:7px;box-shadow:0 10px 14px rgba(0,0,0,.28);font:600 14px "Montserrat",sans-serif;color:var(--gold);display:flex;align-items:center;justify-content:center}
.about-shadow{position:absolute;left:40px;top:835px;width:1120px;height:18px;background:radial-gradient(ellipse at top,rgba(0,0,0,.18),transparent 70%)}

/* services */
.services{position:absolute;left:0;top:1202px;width:1200px;height:468px;overflow:hidden;background:radial-gradient(ellipse 520px 260px at 600px 220px,#3b3a22 0%,#1a1a12 55%,#080806 100%)}
.service{position:absolute;width:250px;font-size:13.3px;line-height:20px;color:var(--white)}
.service h3{font:700 13.3px "Open Sans",sans-serif;text-transform:uppercase}
.svc-ring{position:absolute;width:100px;height:100px;border:3px solid var(--white);border-radius:50%;display:flex;align-items:center;justify-content:center;background:rgba(0,0,0,.35)}
.svc-hub{position:absolute;left:451px;top:225px;width:300px;height:300px;border:4px solid var(--white);border-radius:50%;background:rgba(0,0,0,.3)}
.svc-hub .brand{left:0;top:110px;width:292px;justify-content:center;font-size:48px}
.svc-hub .brand .dot{width:22px;height:22px}

/* pricing */
.plan{position:absolute;top:1807px;width:261px;height:373px;border:1px solid #bdbdbd;background:var(--white)}
.plan-name{position:absolute;top:36px;width:100%;text-align:center;font:400 14px "Open Sans",sans-serif;color:#666;letter-spacing:.5px}
.plan-price{position:absolute;top:62px;width:100%;text-align:center;font:700 italic 46px "Fira Sans",sans-serif;color:var(--gold)}
.plan-body{position:absolute;left:0;top:148px;width:100%;height:224px;background:var(--card-grey)}
.plan-features{list-style:none;position:absolute;left:48px;top:26px}
.plan-features li{display:flex;align-items:center;gap:10px;height:22.5px;font-size:12px;color:#333}
.try-btn{position:absolute;left:37px;top:154px;width:183px;height:37px;background:var(--gold);font:700 italic 18px "Fira Sans",sans-serif;color:var(--white);display:flex;align-items:center;justify-content:center}

/* demo */
.demo{position:absolute;left:0;top:2234px;width:1200px;height:466px;background:var(--grey-bg)}
.devices{position:absolute;left:87px;top:77px;width:394px;height:255px;background:linear-gradient(160deg,#2c2c2c,#0c0c0c 60%,#3a3a3a);border-radius:10px;box-shadow:0 16px 24px rgba(0,0,0,.25)}
.demo-title{position:absolute;left:740px;top:72px;display:flex;align-items:center;gap:18px;font:700 23px "Montserrat",sans-serif}
.demo-title .mark{width:30px;height:30px;border:4px solid var(--gold);border-radius:50%}
.field{position:absolute;height:41px;background:var(--white);font-size:12px;color:#333;padding:12px 14px}
.field.select::after{content:"";position:absolute;right:14px;top:17px;border:7px solid transparent;border-top:8px solid #555}
.submit{position:absolute;left:568px;top:352px;width:215px;height:32px;background:var(--gold);border:1px solid #b89a00;font:700 13px "Open Sans",sans-serif;color:var(--ink);display:flex;align-items:center;justify-content:center}

/* footer */
.footer{position:absolute;left:0;top:2700px;width:1200px;height:367px;background:var(--black)}
.footer-bump{position:absolute;left:470px;top:2672px;width:260px;height:60px;background:var(--black);border-radius:60px 60px 0 0}
.footer .brand{left:0;top:22px;width:1200px;justify-content:center;font-size:46px}
.footer .brand .dot{width:22px;height:22px}
.f-col{position:absolute;top:114px}
.f-col h4{font:700 13px "Montserrat",sans-serif;color:var(--gold);padding-bottom:12px;border-bottom:1px solid #333;width:180px}
.f-col ul{list-style:none;margin-top:20px}
.f-col li{font:600 11.5px "Open Sans",sans-serif;color:var(--white);line-height:20px;text-transform:uppercase}
.f-contact{font:600 11.5px "Open Sans",sans-serif;color:var(--white);line-height:20px}
.f-contact .row{position:absolute;left:0;display:flex;gap:10px}
.f-icon{width:20px;height:20px;border:2px solid var(--gold);border-radius:50%;flex:none;display:flex;align-items:center;justify-content:center}
.f-input{position:absolute;left:0;width:275px;height:28px;background:#1f1f1f;font-size:10.5px;color:var(--white);padding:6px 10px}
.f-submit{position:absolute;left:0;top:293px;width:97px;height:25px;background:var(--gold);font:700 11px "Open Sans",sans-serif;color:var(--white);display:flex;align-items:center;justify-content:center}
.bottom-bar{position:absolute;left:0;top:3067px;width:1200px;height:42px;background:var(--gold);display:flex;align-items:center;justify-content:space-between;padding:0 28px 0 40px;font:600 11px "Open Sans",sans-serif;color:var(--black)}
.bottom-bar .socials{display:flex;gap:8px}
.bottom-bar .socials i{width:24px;height:24px;border:2px solid var(--white);border-radius:50%;display:block}
</style>
</head>
<body>

<svg width="0" height="0" style="position:absolute">
  <defs>
    <symbol id="i-cloud" viewBox="0 0 48 48"><path d="M14 36h21a8 8 0 0 0 1-15.9A12 12 0 0 0 13 18a9 9 0 0 0 1 18z" fill="none" stroke="currentColor" stroke-width="3" stroke-linejoin="round"/></symbol>
    <symbol id="i-computing" viewBox="0 0 48 48"><use href="#i-cloud"/><circle cx="24" cy="26" r="2.5" fill="currentColor"/><circle cx="17" cy="31" r="2" fill="currentColor"/><circle cx="31" cy="31" r="2" fill="currentColor"/><circle cx="24" cy="40" r="2" fill="currentColor"/><path d="M24 26l-7 5M24 26l7 5M24 28v12" stroke="currentColor" stroke-width="1.8"/></symbol>
    <symbol id="i-storage" viewBox="0 0 48 48"><use href="#i-cloud"/><path d="M24 40V22M17 29l7-7 7 7" fill="none" stroke="currentColor" stroke-width="3" stroke-linecap="round" stroke-linejoin="round"/></symbol>
    <symbol id="i-security" viewBox="0 0 48 48"><path d="M14 34h21a8 8 0 0 0 1-15.9A12 12 0 0 0 13 16a9 9 0 0 0 1 18z" fill="currentColor"/><rect x="17" y="27" width="14" height="13" rx="2" fill="#111" stroke="currentColor" stroke-width="2"/><path d="M20 27v-4a4 4 0 0 1 8 0v4" fill="none" stroke="#111" stroke-width="2.5"/><circle cx="24" cy="33" r="1.8" fill="currentColor"/></symbol>
    <symbol id="i-processing" viewBox="0 0 48 48"><use href="#i-cloud"/><path d="M18 28a6 6 0 0 1 11-3M30 30a6 6 0 0 1-11 3" fill="none" stroke="currentColor" stroke-width="2.5" stroke-linecap="round"/><path d="M29 21v4h-4M19 37v-4h4" fill="none" stroke="currentColor" stroke-width="2.5" stroke-linecap="round"/></symbol>
    <symbol id="i-tick" viewBox="0 0 16 16"><path d="M2 8.5l4 4L14 3" fill="none" stroke="#7cb518" stroke-width="3" stroke-linecap="round" stroke-linejoin="round"/></symbol>
    <symbol id="i-phone" viewBox="0 0 16 16"><path d="M4 2l3 3-1.5 2a8 8 0 0 0 3.5 3.5L11 9l3 3-2 2C7 14 2 9 2 4z" fill="currentColor"/></symbol>
    <symbol id="i-mail" viewBox="0 0 16 16"><rect x="2" y="4" width="12" height="9" rx="1" fill="none" stroke="currentColor" stroke-width="1.6"/><path d="M2 5l6 4 6-4" fill="none" stroke="currentColor" stroke-width="1.6"/></symbol>
    <symbol id="i-pin" viewBox="0 0 16 16"><path d="M8 15s-5-5.5-5-9a5 5 0 0 1 10 0c0 3.5-5 9-5 9z" fill="currentColor"/><circle cx="8" cy="6" r="2" fill="#000"/></symbol>
  </defs>
</svg>

<!-- Hero -->
<section class="hero">
  <div class="hero-photo" role="img" aria-label="Businessman holding a tablet with glowing cloud computing network icons floating above it"></div>
  <h1 class="hero-title">REVOLUTIONIZING THE ENTIRE COMPUTER INDUSTRY</h1>
  <div class="hero-cta">GET STARTED</div>
</section>

<header class="site-header">
  <div class="contact-tab">
    <span><i class="tab-icon"><svg width="11" height="11" style="color:#000"><use href="#i-phone"/></svg></i>1-800-555-0142</span>
    <span><i class="tab-icon"><svg width="11" height="11" style="color:#000"><use href="#i-mail"/></svg></i>info@uvanta.com</span>
    <span class="tab-social"><i></i><i></i><i></i></span>
  </div>
  <div class="brand"><span class="dot"></span>UVANTA</div>
  <nav class="main-nav">
    <a class="active" style="left:0">HOME</a>
    <a style="left:73px">ABOUT</a>
    <a style="left:150px">SERVICES</a>
    <a style="left:239px">PRICING</a>
    <a style="left:326px">CONTACT</a>
  </nav>
  <div class="demo-btn">Request A Demo</div>
</header>

<!-- Feature band -->
<section class="feature-band"></section>
<div class="band-title">REVOLUTIONIZING</div>
<div class="band-sub"><b>THE ENTIRE</b> COMPUTER INDUSTRY</div>
<div class="feature" style="left:556px"><div class="ring"><svg width="50" height="50" style="color:var(--gold)"><use href="#i-computing"/></svg></div><div class="label">COMPUTING</div></div>
<div class="feature" style="left:703px"><div class="ring"><svg width="50" height="50" style="color:var(--gold)"><use href="#i-storage"/></svg></div><div class="label">STORAGE</div></div>
<div class="feature" style="left:850px"><div class="ring"><svg width="50" height="50" style="color:var(--gold)"><use href="#i-security"/></svg></div><div class="label">SECURITY</div></div>
<div class="feature" style="left:999px"><div class="ring"><svg width="50" height="50" style="color:var(--gold)"><use href="#i-processing"/></svg></div><div class="label">PROCESSING</div></div>

<!-- About -->
<div class="about-shadow"></div>
<h2 class="sec-title" style="top:893px"><span class="rule"></span><span class="mark"></span>ABOUT UVANTA<span class="rule"></span></h2>
<p class="about-text">Lorem ipsum dolor sit amet, consectetuer adipiscing elit, sed diam nonummy nibh euismod tincidunt ut laoreet dolore magna aliquam erat volutpat. Ut wisi enim ad minim veniam, quis nostrud exerci tation ullamcorper suscipit lobortis nisl ut aliquip ex ea commodo consequat. Duis autem vel eum iriure dolor in hendrerit in vulputate velit esse molestie consequat, vel illum dolore eu feugiat nulla facilisis at vero eros et accumsan et iusto odio dignissim qui blandit praesent luptatum zzril delenit augue duis dolore te feugait nulla facilisi.</p>
<div class="learn-btn">Learn More</div>

<!-- Services -->
<section class="services" role="img" aria-label="Dark background photo of a hand touching a glowing digital interface" >
  <h2 class="sec-title" style="top:60px;color:var(--white)"><span class="rule" style="background:#777"></span><span class="mark"></span>SERVICES<span class="rule" style="background:#777"></span></h2>
  <svg class="abs" style="left:0;top:0" width="1200" height="468">
    <path d="M427 197 L520 250 M427 350 L470 350 M773 197 L680 250 M773 350 L730 350" stroke="#fff" stroke-width="2" fill="none"/>
  </svg>
  <div class="service" style="left:73px;top:156px"><h3>Cloud Computing</h3>Lorem ipsum dolor sit amet, consec tetuer adipiscing elit, sed diam non ummy nibh euismod tincidunt.</div>
  <div class="service" style="left:73px;top:310px"><h3>Cloud Storage</h3>Lorem ipsum dolor sit amet, consec tetuer adipiscing elit, sed diam non ummy nibh euismod tincidunt.</div>
  <div class="service" style="left:889px;top:156px"><h3>Security</h3>Lorem ipsum dolor sit amet, consec tetuer adipiscing elit, sed diam non ummy nibh euismod tincidunt.</div>
  <div class="service" style="left:889px;top:310px"><h3>Cloud Processing</h3>Lorem ipsum dolor sit amet, consec tetuer adipiscing elit, sed diam non ummy nibh euismod tincidunt.</div>
  <div class="svc-ring" style="left:327px;top:147px"><svg width="60" height="60" style="color:var(--gold)"><use href="#i-computing"/></svg></div>
  <div class="svc-ring" style="left:327px;top:300px"><svg width="60" height="60" style="color:var(--gold)"><use href="#i-storage"/></svg></div>
  <div class="svc-ring" style="left:773px;top:147px"><svg width="60" height="60" style="color:var(--gold)"><use href="#i-security"/></svg></div>
  <div class="svc-ring" style="left:773px;top:300px"><svg width="60" height="60" style="color:var(--gold)"><use href="#i-processing"/></svg></div>
  <div class="svc-hub"><div class="brand"><span class="dot"></span>UVANTA</div></div>
</section>

<!-- Pricing -->
<h2 class="sec-title" style="top:1729px"><span class="rule"></span><span class="mark"></span>PRICING<span class="rule"></span></h2>

<div class="plan" style="left:56px">
  <div class="plan-name">LITE</div><div class="plan-price">$39/mo</div>
  <div class="plan-body"><ul class="plan-features"><li><svg width="14" height="14"><use href="#i-tick"/></svg>Cloud Computing</li><li><svg width="14" height="14"><use href="#i-tick"/></svg>Cloud Storage</li><li><svg width="14" height="14"><use href="#i-tick"/></svg>Security</li><li><svg width="14" height="14"><use href="#i-tick"/></svg>Cloud Processing</li></ul><div class="try-btn">TRY FOR FREE</div></div>
</div>
<div class="plan" style="left:332px">
  <div class="plan-name">PRO</div><div class="plan-price">$79/mo</div>
  <div class="plan-body"><ul class="plan-features"><li><svg width="14" height="14"><use href="#i-tick"/></svg>Cloud Computing</li><li><svg width="14" height="14"><use href="#i-tick"/></svg>Cloud Storage</li><li><svg width="14" height="14"><use href="#i-tick"/></svg>Security</li><li><svg width="14" height="14"><use href="#i-tick"/></svg>Cloud Processing</li></ul><div class="try-btn">TRY FOR FREE</div></div>
</div>
<div class="plan" style="left:607px">
  <div class="plan-name">TEAM</div><div class="plan-price">$119/mo</div>
  <div class="plan-body"><ul class="plan-features"><li><svg width="14" height="14"><use href="#i-tick"/></svg>Cloud Computing</li><li><svg width="14" height="14"><use href="#i-tick"/></svg>Cloud Storage</li><li><svg width="14" height="14"><use href="#i-tick"/></svg>Security</li><li><svg width="14" height="14"><use href="#i-tick"/></svg>Cloud Processing</li></ul><div class="try-btn">TRY FOR FREE</div></div>
</div>
<div class="plan" style="left:885px">
  <div class="plan-name">ENTERPRISE</div><div class="plan-price">$149/mo</div>
  <div class="plan-body"><ul class="plan-features"><li><svg width="14" height="14"><use href="#i-tick"/></svg>Cloud Computing</li><li><svg width="14" height="14"><use href="#i-tick"/></svg>Cloud Storage</li><li><svg width="14" height="14"><use href="#i-tick"/></svg>Security</li><li><svg width="14" height="14"><use href="#i-tick"/></svg>Cloud Processing</li></ul><div class="try-btn">TRY FOR FREE</div></div>
</div>

<!-- Request a demo -->
<section class="demo">
  <div class="devices" role="img" aria-label="Desktop monitor, tablet and smartphone showing the brand on black screens"></div>
  <h2 class="demo-title"><span class="mark"></span>REQUEST A DEMO</h2>
  <div class="field" style="left:566px;top:137px;width:288px">Name</div>
  <div class="field" style="left:862px;top:137px;width:284px">Email Address</div>
  <div class="field" style="left:566px;top:191px;width:288px">Phone</div>
  <div class="field select" style="left:862px;top:191px;width:284px">Interested In</div>
  <div class="field" style="left:566px;top:245px;width:580px;height:95px">Message</div>
  <div class="submit">SUBMIT</div>
</section>

<!-- Footer -->
<div class="footer-bump"></div>
<footer class="footer">
  <div class="brand"><span class="dot"></span>UVANTA</div>
  <div class="f-col" style="left:128px">
    <h4>QUICK LINKS</h4>
    <ul><li>Home</li><li>About</li><li>Services</li><li>Pricing</li><li>Contact</li><li>Request A Demo</li></ul>
  </div>
  <div class="f-col" style="left:327px">
    <h4>SERVICES</h4>
    <ul><li>Cloud Computing</li><li>Cloud Storage</li><li>Security</li><li>Cloud Processing</li></ul>
  </div>
  <div class="f-col f-contact" style="left:535px">
    <h4>CONTACT</h4>
    <div class="row" style="top:52px"><i class="f-icon"><svg width="11" height="11" style="color:var(--gold)"><use href="#i-pin"/></svg></i><div>UVANTA<br>48 HARBOR LANE DR<br>SUITE 310<br>FAIRVIEW, CA 90418</div></div>
    <div class="row" style="top:152px"><i class="f-icon"><svg width="11" height="11" style="color:var(--gold)"><use href="#i-phone"/></svg></i><div>(800) 555-0142</div></div>
    <div class="row" style="top:192px"><i class="f-icon"><svg width="11" height="11" style="color:var(--gold)"><use href="#i-mail"/></svg></i><div>info@uvanta.com</div></div>
  </div>
  <div class="f-col" style="left:796px">
    <h4 style="width:275px">SEND US A MESSAGE</h4>
    <div class="f-input" style="top:46px">Name</div>
    <div class="f-input" style="top:81px">Email</div>
    <div class="f-input" style="top:110px;height:61px">Message</div>
    <div class="f-submit" style="top:179px">SUBMIT</div>
  </div>
</footer>
<div class="bottom-bar">
  <span>COPYRIGHT © 2017 UVANTA. ALL RIGHTS RESERVED.</span>
  <span class="socials"><i></i><i></i><i></i></span>
</div>

</body>
</html>
```